Modern Venture Capital website

Design a modern website for a venture capital firm. This website should be modern and beautiful and be on par with other Venture Capital websites. I have a logo and a hero video I'd like to use. Link to hero video: https://files.vantoria.example/f/9Xk2Lm7qPz4Rt8Wb3Nc6Hd5Jy1Gs0Ve/view?ref=share_link

Preference will be given to the best design that combines design with the best images and digital content. That means no generic free stock videos 😅

I currently built a wix website to give you an idea of what content needs to be on the website. Depending on your design it can be 3 pages, or one long page. I will leave it up to you.

WEBSITE: https://brelmor58204.pagecraftly.example/my-site-4

Target Market(s)

Mid-career professionals, individuals interested in Venture Capital

Industry/Entity Type

Finance, venture capital, startups

Requirements
Must have
• must use the hero video I have and must use my logo. Must use high quality images that matches the website design - no generic stock images

```html
<!DOCTYPE html>
<html lang="en">
<head>
<meta charset="utf-8">
<title>Nightfall Capital — Venture Capital for the late night hustlers</title>
<link rel="stylesheet" href="https://fonts.googleapis.com/css2?family=Poppins:wght@300;400;500;600;700&display=swap">
<style>
:root{
  --bg:#0a0a0c;
  --bg-soft:#141416;
  --bg-contact:#1c1c1e;
  --ink:#ffffff;
  --muted:#b9b9bd;
  --dim:#8a8a90;
  --accent:#f26a2e;
  --accent-deep:#c8461a;
  --line:#3a3a3e;
}
*{box-sizing:border-box;margin:0;padding:0}
html,body{width:1200px;height:4192px;overflow:hidden;background:var(--bg);color:var(--ink);font-family:'Poppins',sans-serif}
.page{position:relative;width:1200px;height:4192px;overflow:hidden;background:var(--bg)}
.abs{position:absolute}
.btn{position:absolute;display:flex;align-items:center;justify-content:center;background:var(--accent);color:#fff;font-size:13px;font-weight:600;border-radius:6px;letter-spacing:.5px}

/* header */
.topbar{top:12px;right:112px;display:flex;gap:28px;font-size:12px;color:var(--muted)}
.topbar span{display:flex;align-items:center;gap:8px}
.logo{font-weight:700;color:#fff;line-height:1}
.logo small{display:block;font-size:.36em;font-weight:700;letter-spacing:4px;margin-top:4px}
.site-logo{top:40px;left:112px;font-size:30px}
.nav{top:50px;left:456px;display:flex;gap:62px;font-size:14px;color:#ddd}
.nav-cta{top:44px;left:944px;width:144px;height:36px;background:#fff;color:#111;font-size:12px}

/* hero */
.hero-media{top:0;left:0;width:1200px;height:640px;background:
 radial-gradient(circle at 620px 330px,#6b3e22 0,#3a2416 70px,transparent 72px),
 radial-gradient(ellipse at 900px 520px,rgba(242,120,50,.35),transparent 60%),
 linear-gradient(180deg,#08080b 0%,#111118 55%,#2b1e1a 82%,#0a0a0c 100%)}
.hero-title{top:250px;left:112px;font-size:52px;font-weight:300;line-height:1.2}
.hero-title strong{font-weight:600;display:block}
.hero-sub{top:398px;left:112px;font-size:22px;font-weight:500}
.hero-btn{top:456px;left:112px;width:188px;height:52px}

/* become a vc */
.section-title{left:0;width:1200px;text-align:center;font-weight:600}
.section-lead{left:330px;width:540px;text-align:center;font-size:12px;line-height:1.6;color:var(--muted)}
.card-media{width:460px;border-radius:2px}
.card-title{font-size:20px;font-weight:500;line-height:1.3}
.card-title.accent{color:var(--accent)}
.card-text{font-size:12px;line-height:1.6;color:var(--muted);width:420px}

/* founders */
.founders-title{top:1950px;left:112px;font-size:44px;font-weight:600;line-height:1.15}
.founders-text{left:112px;width:470px;font-size:12px;line-height:1.7;color:var(--muted)}
.moon-large{top:1880px;left:720px;width:470px;height:470px;border-radius:50%;background:radial-gradient(circle at 40% 40%,#c9c9cc 0%,#8d8d92 40%,#4b4b50 75%,#222 100%);box-shadow:-20px -10px 80px rgba(242,130,60,.45)}

/* fund economics */
.fund-title{top:2470px;left:120px;font-size:64px;font-weight:600;color:transparent;-webkit-text-stroke:1.5px #9a9aa0}
.stat{position:absolute;text-align:center;width:160px}
.stat b{display:block;font-size:56px;font-weight:600;line-height:1}
.stat span{display:block;font-size:12px;color:var(--muted);margin-top:8px;line-height:1.3}

/* partners */
.partner{position:absolute;top:3020px;height:40px;width:130px;border-radius:6px;background:#3a3a3e}
.planet{top:3120px;left:420px;width:360px;height:360px;border-radius:50%;background:radial-gradient(circle at 50% 35%,#6a6a70 0%,#37373c 45%,#151518 80%);opacity:.75}

/* contact */
.contact{top:3420px;left:0;width:1200px;height:400px;background:var(--bg-contact)}
.field-label{position:absolute;font-size:12px;color:#ddd}
.field-line{position:absolute;height:1px;background:#55555a}

/* footer */
.footer-head{font-size:14px;font-weight:500;color:#fff}
.footer-list{font-size:12px;color:var(--muted);line-height:2.2}
.copyright{top:4152px;left:0;width:1200px;text-align:center;font-size:12px;color:#bbb}
</style>
</head>
<body>
<div class="page">

  <!-- Hero -->
  <div class="abs hero-media" role="img" aria-label="Night city skyline with a large moon rising over lit towers"></div>
  <div class="abs topbar">
    <span><svg width="12" height="12" viewBox="0 0 24 24" fill="#fff"><path d="M6.6 10.8a15 15 0 0 0 6.6 6.6l2.2-2.2a1 1 0 0 1 1-.25 11.4 11.4 0 0 0 3.6.57 1 1 0 0 1 1 1V20a1 1 0 0 1-1 1A17 17 0 0 1 3 4a1 1 0 0 1 1-1h3.5a1 1 0 0 1 1 1c0 1.25.2 2.45.57 3.6a1 1 0 0 1-.25 1z"/></svg>555-014-2290</span>
    <span><svg width="13" height="12" viewBox="0 0 24 20" fill="none" stroke="#fff" stroke-width="2"><rect x="1" y="1" width="22" height="18" rx="2"/><path d="M1 3l11 8 11-8"/></svg>hello@nightfallcap.example</span>
  </div>
  <div class="abs logo site-logo">Nightfall<small>CAPITAL</small></div>
  <nav class="abs nav"><span>Home</span><span>About</span><span>Services</span><span>Contact</span></nav>
  <div class="btn nav-cta">GET STARTED</div>

  <h1 class="abs hero-title">Venture Capital for the <strong>late night hustlers</strong></h1>
  <p class="abs hero-sub">Become a Venture Capital Investor</p>
  <div class="btn hero-btn">LEARN MORE</div>

  <svg class="abs" style="top:560px;left:0" width="1200" height="110" viewBox="0 0 1200 110">
    <polygon points="0,110 600,30 1200,110 1200,96 600,18 0,96" fill="var(--accent)"/>
    <polygon points="0,110 600,40 1200,110" fill="var(--bg)"/>
    <circle cx="600" cy="44" r="24" fill="#fff"/>
    <path d="M590 40l10 10 10-10" fill="none" stroke="#111" stroke-width="3"/>
  </svg>

  <!-- Become a VC -->
  <h2 class="abs section-title" style="top:690px;font-size:40px">Become a VC</h2>
  <p class="abs section-lead" style="top:752px">At Nightfall Capital, we're opening the doors to a new kind of investor, mid-career professionals and aspiring VCs who want real skin in the game, not just exposure from the sidelines.</p>

  <div class="abs card-media" style="top:852px;left:112px;height:320px;background:linear-gradient(160deg,#2a2430,#4a3322 55%,#0e0d10)" role="img" aria-label="City street at night with glowing high-rise towers"></div>
  <div class="abs card-media" style="top:852px;left:628px;height:320px;background:linear-gradient(120deg,#b8b8bc 0%,#5d5d62 42%,#18243a 60%,#0b1020 100%)" role="img" aria-label="Full moon beside a professional working at night"></div>
  <h3 class="abs card-title" style="top:1206px;left:112px">Hands on VC Work</h3>
  <p class="abs card-text" style="top:1240px;left:112px">Each Nightfall investor can actively be involved in sourcing, evaluating, and making key investment decisions as little or as much as they want.</p>
  <h3 class="abs card-title accent" style="top:1206px;left:628px">Earn Carry and Put Your Name on<br>an Investment</h3>
  <p class="abs card-text" style="top:1266px;left:628px">Each Nightfall investor can actively be involved in sourcing, evaluating, and making key investment decisions.</p>

  <div class="abs card-media" style="top:1380px;left:112px;height:332px;background:linear-gradient(150deg,#4a2c18,#1e1a1c 50%,#0c0c10)" role="img" aria-label="Professional in a suit standing in front of city lights"></div>
  <div class="abs card-media" style="top:1380px;left:628px;height:332px;background:linear-gradient(160deg,#1a2030,#2c3a52 45%,#0c0f18)" role="img" aria-label="Professional working on a laptop late at night"></div>
  <h3 class="abs card-title" style="top:1740px;left:112px">Meaningful Opportunities to develop<br>your career in Venture Capital</h3>
  <p class="abs card-text" style="top:1800px;left:112px">Each Nightfall investor can actively be involved in sourcing, evaluating, and making key.</p>
  <h3 class="abs card-title" style="top:1740px;left:628px">Join a community of<br>Hustlers</h3>
  <p class="abs card-text" style="top:1800px;left:628px">Each Nightfall investor can actively be involved in sourcing, evaluating, and making key investment decisions.</p>

  <!-- Founders -->
  <div class="abs moon-large" role="img" aria-label="Moon lit from behind by a warm sunrise glow"></div>
  <h2 class="abs founders-title">Simplifying Success<br>For Founders</h2>
  <p class="abs founders-text" style="top:2070px">Our strength lies in our network. Our LPs and operating partners are all mid-to-senior level executives in their industries. They bring real-world corporate experience, offering strategic insights and operational support to help our portfolio companies scale efficiently.</p>
  <p class="abs founders-text" style="top:2160px">We cut through the noise and get to the core of your business fast. If we love what you're building, we'll move. If not, we'll tell you quickly and respectfully. That lets you make</p>
  <div class="btn" style="top:2226px;left:112px;width:188px;height:52px">LEARN MORE</div>

  <!-- Fund Economics -->
  <svg class="abs" style="top:2400px;left:0" width="1200" height="400" viewBox="0 0 1200 400">
    <polyline points="128,48 128,344 330,344 370,320 520,320 560,292 700,292 740,262 880,262 920,232 1088,232" fill="none" stroke="var(--accent)" stroke-width="3"/>
    <circle cx="128" cy="48" r="14" fill="#fff" stroke="var(--accent)" stroke-width="4"/>
    <circle cx="1088" cy="232" r="14" fill="#fff" stroke="var(--accent)" stroke-width="4"/>
  </svg>
  <h2 class="abs fund-title">Fund Economics</h2>
  <div class="stat" style="top:2716px;left:152px"><b>14</b><span>Pre-Seed / Seed<br>Investments</span></div>
  <div class="stat" style="top:2716px;left:340px"><b>50k</b><span>Check Size</span></div>
  <div class="stat" style="top:2654px;left:530px"><b>20%</b><span>Carried Interest</span></div>
  <div class="stat" style="top:2624px;left:716px"><b>2.5%</b><span>Management Fee</span></div>
  <div class="stat" style="top:2594px;left:900px"><b>1M</b><span>Fund Size</span></div>

  <!-- Partners -->
  <div class="abs planet" role="img" aria-label="Dim planet surface glowing in dark space"></div>
  <h2 class="abs section-title" style="top:2890px;font-size:40px">Our Partners</h2>
  <p class="abs section-lead" style="top:2950px">At Nightfall Capital, we're opening the doors to a new kind of investor, mid-career professionals and aspiring VCs who want real skin in the game, not just exposure from the sidelines.</p>
  <div class="partner" style="left:260px"></div>
  <div class="partner" style="left:450px"></div>
  <div class="partner" style="left:640px"></div>
  <div class="partner" style="left:810px"></div>

  <h2 class="abs section-title" style="top:3172px;font-size:40px">Ready To Start Investing As A VC?</h2>
  <p class="abs section-lead" style="top:3236px">Book an intro call to learn more and see if you qualify.</p>
  <div class="btn" style="top:3286px;left:512px;width:176px;height:50px">GET STARTED</div>

  <!-- Contact -->
  <section class="abs contact">
    <p class="abs" style="top:62px;left:112px;font-size:14px">Contact</p>
    <h2 class="abs" style="top:88px;left:112px;font-size:46px;font-weight:600">Get In Touch</h2>
    <span class="field-label" style="top:186px;left:112px">First Name*</span>
    <span class="field-label" style="top:186px;left:352px">Last Name*</span>
    <span class="field-label" style="top:186px;left:592px">Message*</span>
    <div class="field-line" style="top:220px;left:112px;width:220px"></div>
    <div class="field-line" style="top:220px;left:352px;width:220px"></div>
    <div class="field-line" style="top:220px;left:592px;width:220px"></div>
    <span class="field-label" style="top:256px;left:112px">Phone Number*</span>
    <span class="field-label" style="top:256px;left:352px">Email Address*</span>
    <div class="field-line" style="top:290px;left:112px;width:220px"></div>
    <div class="field-line" style="top:290px;left:352px;width:220px"></div>
    <div class="field-line" style="top:290px;left:592px;width:220px"></div>
    <div class="btn" style="top:248px;left:824px;width:264px;height:40px">SEND MESSAGE</div>
  </section>

  <!-- Footer -->
  <svg class="abs" style="top:3800px;left:0" width="1200" height="60" viewBox="0 0 1200 60">
    <polygon points="0,0 1200,0 1200,30 900,6 600,40 300,6 0,30" fill="var(--bg-contact)"/>
    <polygon points="0,30 300,6 600,40 900,6 1200,30 1200,40 900,16 600,52 300,16 0,40" fill="var(--accent)"/>
  </svg>
  <div class="abs logo" style="top:3966px;left:112px;font-size:34px">Nightfall<small>CAPITAL</small></div>
  <div class="abs" style="top:3928px;left:400px">
    <p class="footer-head">Quick Links</p>
    <div class="footer-list" style="margin-top:10px">Vision<br>Programs<br>Blog</div>
  </div>
  <div class="abs" style="top:3928px;left:600px">
    <p class="footer-head">Follow Us On</p>
    <div style="display:flex;gap:18px;margin-top:20px">
      <span style="width:14px;height:14px;border-radius:50%;background:#ddd"></span>
      <span style="width:14px;height:14px;border-radius:50%;background:#ddd"></span>
      <span style="width:14px;height:14px;border-radius:50%;background:#ddd"></span>
    </div>
  </div>
  <div class="abs" style="top:3928px;left:826px">
    <p class="footer-head">Contact Us</p>
    <div class="footer-list" style="margin-top:10px">
      <div style="display:flex;align-items:center;gap:10px"><svg width="12" height="12" viewBox="0 0 24 24" fill="#fff"><path d="M6.6 10.8a15 15 0 0 0 6.6 6.6l2.2-2.2a1 1 0 0 1 1-.25 11.4 11.4 0 0 0 3.6.57 1 1 0 0 1 1 1V20a1 1 0 0 1-1 1A17 17 0 0 1 3 4a1 1 0 0 1 1-1h3.5a1 1 0 0 1 1 1c0 1.25.2 2.45.57 3.6a1 1 0 0 1-.25 1z"/></svg>555-014-2290</div>
      <div style="display:flex;align-items:center;gap:10px"><svg width="13" height="12" viewBox="0 0 24 20" fill="none" stroke="#fff" stroke-width="2"><rect x="1" y="1" width="22" height="18" rx="2"/><path d="M1 3l11 8 11-8"/></svg>hello@nightfallcap.example</div>
    </div>
    <div style="width:240px;height:1px;background:#555;margin-top:8px"></div>
  </div>
  <div class="abs" style="top:4120px;left:112px;width:976px;height:1px;background:#333"></div>
  <p class="abs copyright">Copyright © nightfall 2023 &nbsp;|&nbsp; All Rights Reserved</p>

</div>
</body>
</html>
```